Header-Bild für Kreditvergleich-Domain
#56 Das Hintergrundbild hat nichts mit Kreditvergleich zu tun
Und bitte die 1. Zeile alle Buchstaben groß schreiben
#49 Bitte mit anderer Schrift, bzw. anderes Logo. Das sieht noch nicht professionell aus
#33 Idee des Headers ist nicht schlecht. Die Frau vermittelt einen zu legeren Umgang mit Krediten.
Der Schriftzug passt leider gar nicht. Er wirkt nicht seriös. "Einfach und sicher sparen" passt nicht so richtig zum Kreditthema.
Kommentar für alle noch vorhandenen Designvorschläge:
Wichtig ist mir, dass das Layout seriös wirkt. Es handelt sich um eine Vergleichsportal für Kredite. Das Layout soll nicht übertrieben, sondern seriös wirken.
Das oder die Bilder müssen eindeutig zu dem Kreditthema passen.
#24 das geht mal gar nicht.... Das Bild sieht absolut billig aus.
#22 Ist immer noch Urlaub und nicht Finanz.
Die eckigen Bilder sehen übrigens besser aus, als das abgerundete Bild.
#19 Die Farbgebung von grün und weiß ist sehr schön. Was nicht passt, ist ein Apfel bei einer Finanzwebseite. Ich dachte hier zuerst an ein Ernährungsportal. Die Farbe gelb des Logos beisst sich etwas mit dem Rest.
Die Grundidee ist aber nicht schlecht.
#18 Bitte andere Farbgebung probieren. So wie die Farbe ist, passt es nicht zum restlichen Layout.
#16: Layout sehr gut gemacht, aber die Bilder müssen seriös wirken und zu Finanzthemen passen.
#7 und #10
diese beiden Header gefallen mir an sich am besten.
Meine Vorstellungen bezüglich der Übergänge sind leider nicht so geworden, wie ich mir das vorgestellt hatte. Deshalb lassen wir Übergänge ab jetzt weg.
#7: Das Logo und die Schrift ist prima. Vielleicht könnte man mal 2-3 andere Hintergrundbilder verwenden. Etwas heller in der Farbe wäre klasse.
#10: Das Logo und die Schrift ist prima, das Bild aber unpassend. Vielleicht könnte man mal 2-3 andere Hintergrundbilder verwenden.
Danke
Die Übergänge sehen irgendwie nicht sehr gut aus. Das geht bestimmt noch besser.
Der Einkaufswagen wirkt nicht sehr seriös
Das Bild gefällt mir schon mal sehr gut.
An paar Anmerkungen dazu:
1. gut ist, dass der kleine Spruch oben links auf bild Nr. 3 nicht mehr dabei ist
2. Der Logo charakter und das Euro zeichen sind prima
3. Wäre mal möglich, die schrift im dem Logo etwas höher zu setzen?
4. Was bei Nr. 7 irgendwie noch fehlt sind die fließendere Übergänge auf der linken und rechten Seite. Der Übergang ist zu hart.

```html
<!DOCTYPE html>
<html lang="de">
<head>
<meta charset="utf-8">
<title>Zinsvista.net – Ihr Kredit Vergleichsportal</title>
<link rel="stylesheet" href="https://fonts.googleapis.com/css2?family=Arimo:wght@400;700&family=Noto+Sans:wght@400;700&display=swap">
<style>
:root{
  --green:#6f9a1e;
  --green-soft:#86a84a;
  --nav-bg:#e3ecd6;
  --nav-line:#ffffff;
  --nav-spacer:#cfe2b1;
  --nav-head:#f4f5f0;
  --side-bg:#e6efd9;
  --text:#222;
  --muted:#555;
  --box-bg:#d9ebb6;
  --box-line:#a8cb63;
  --logo-bg:#2b2e30;
}
*{margin:0;padding:0;box-sizing:border-box}
html,body{width:1200px;height:1200px;overflow:hidden;background:#fff}
body{font-family:"Noto Sans",Verdana,sans-serif;color:var(--text)}
.page{position:relative;width:1200px;height:1200px}
.header{position:absolute;left:0;top:0;width:1200px;height:172px;
  background:linear-gradient(90deg,#7f9eb0 0%,#9fc3d0 20%,#6fb4c4 45%,#58a8bb 65%,#c9c1a4 85%,#e1d6b8 100%)}
.logo-box{position:absolute;left:765px;top:22px;width:405px;height:125px;border-radius:18px;
  background:var(--logo-bg);opacity:.88;display:flex;flex-direction:column;justify-content:center;align-items:flex-end;padding-right:28px}
.logo-name{font-family:"Arimo",sans-serif;font-weight:700;font-size:44px;color:#fff;line-height:1}
.logo-claim{font-family:"Arimo",sans-serif;font-weight:700;font-size:22px;color:#fff;margin-top:10px}
.nav{position:absolute;left:0;top:175px;width:250px;height:437px;background:var(--nav-bg);overflow:hidden}
.nav-head{height:35px;background:var(--nav-head);font-weight:700;font-size:14px;padding:9px 16px;border-bottom:1px solid var(--nav-line)}
.nav-item{height:35px;font-size:13px;color:var(--muted);padding:9px 16px;border-bottom:2px solid var(--nav-line)}
.nav-spacer{height:30px;background:var(--nav-spacer)}
.main{position:absolute;left:250px;top:172px;width:690px;height:440px}
.title{position:absolute;left:0;width:690px;top:4px;text-align:center;font-family:"Arimo",sans-serif;font-weight:700;font-size:24px;color:var(--green)}
.subtitle{position:absolute;left:0;width:690px;top:48px;text-align:center;font-family:"Arimo",sans-serif;font-size:22px;color:var(--green-soft);letter-spacing:1px}
.money{position:absolute;left:35px;top:126px;width:216px;height:162px;border:1px solid #999;padding:6px}
.money div{width:100%;height:100%;background:linear-gradient(160deg,#eef2ea,#9dbf8a 50%,#5f7f58)}
.intro{position:absolute;left:269px;top:120px;width:400px;font-size:14px;line-height:22px}
.notice{position:absolute;left:35px;top:325px;width:621px;height:72px;background:var(--box-bg);border:1px solid var(--box-line);border-radius:4px;padding:6px 12px;font-size:13.5px;line-height:21px}
.rule{position:absolute;left:35px;top:433px;width:621px;border-top:2px dotted #e3c8b8}
.side{position:absolute;left:940px;top:172px;width:260px;height:440px;background:var(--side-bg);padding:12px 15px}
.side h2{font-size:15px;font-weight:700;color:#444;margin-top:8px;margin-bottom:12px}
.perk{font-size:12.5px;line-height:19px;margin-bottom:19px}
.perk svg{vertical-align:-2px;margin-right:4px}
.side h3{font-size:15px;font-weight:700;color:#444;position:absolute;top:408px;left:15px}
</style>
</head>
<body>
<div class="page">
  <header class="header" role="img" aria-label="Strandpanorama mit Villa, Sportwagen, Pool und Palmen">
    <div class="logo-box">
      <div class="logo-name">Zinsvista.net</div>
      <div class="logo-claim">Ihr Kredit Vergleichsportal</div>
    </div>
  </header>

  <nav class="nav">
    <div class="nav-head">Ratenkredit</div>
    <div class="nav-item">Crestmoor Bank</div>
    <div class="nav-item">Eurovale Bank</div>
    <div class="nav-item">Nordhag Bank</div>
    <div class="nav-spacer"></div>
    <div class="nav-head">Kleinkredit</div>
    <div class="nav-item">Crestmoor Bank</div>
    <div class="nav-item">Lindquay Bank</div>
    <div class="nav-item">&nbsp;Eurovale Bank</div>
    <div class="nav-spacer"></div>
    <div class="nav-head">Autokredit</div>
    <div class="nav-item">Eurovale Bank</div>
    <div class="nav-item">Crestmoor Bank</div>
  </nav>

  <main class="main">
    <h1 class="title">Zinsvista.net - Ihr Kredit Vergleichsportal</h1>
    <p class="subtitle">- Der unabhängige Kredit Vergleich -</p>
    <div class="money"><div role="img" aria-label="Gestapelte Euro-Geldscheinbündel"></div></div>
    <p class="intro">Sie wollen sich Ihre Wünsche jetzt gleich erfüllen? Ein Kredit mit festem Zins und gleich bleibenden Raten ist oft deutlich günstiger als ein überzogenes Girokonto. Wenn sie Kredite gründlich vergleichen, sparen Sie viel Geld. Finden Sie bei uns attraktive Kredite schnell und einfach online.</p>
    <p class="notice">Profitieren Sie vom Wettbewerb unter den Kreditanbietern, denn Onlinebanken können aufgrund des Verzichts auf teure Filialen sehr günstige Zinsen anbieten. Trotzdem ist ein sehr guter Service per Telefon oder Internet gegeben.</p>
    <div class="rule"></div>
  </main>

  <aside class="side">
    <h2>Ihre Kredit Vorteile</h2>
    <p class="perk"><svg width="20" height="18" viewBox="0 0 20 18"><path d="M2 10l5 5L18 2" fill="none" stroke="#8cc43c" stroke-width="4" stroke-linecap="round"/></svg>Wünsche gleich erfüllen können</p>
    <p class="perk"><svg width="20" height="18" viewBox="0 0 20 18"><path d="M2 10l5 5L18 2" fill="none" stroke="#8cc43c" stroke-width="4" stroke-linecap="round"/></svg>einfache Finanzierung über das Internet</p>
    <p class="perk"><svg width="20" height="18" viewBox="0 0 20 18"><path d="M2 10l5 5L18 2" fill="none" stroke="#8cc43c" stroke-width="4" stroke-linecap="round"/></svg>vom Wettbewerb der Banken profitieren</p>
    <p class="perk"><svg width="20" height="18" viewBox="0 0 20 18"><path d="M2 10l5 5L18 2" fill="none" stroke="#8cc43c" stroke-width="4" stroke-linecap="round"/></svg>günstige Zinsen durch Banken ohne Filialen</p>
    <p class="perk"><svg width="20" height="18" viewBox="0 0 20 18"><path d="M2 10l5 5L18 2" fill="none" stroke="#8cc43c" stroke-width="4" stroke-linecap="round"/></svg>sicher, schnell, einfach</p>
    <p class="perk"><svg width="20" height="18" viewBox="0 0 20 18"><path d="M2 10l5 5L18 2" fill="none" stroke="#8cc43c" stroke-width="4" stroke-linecap="round"/></svg>kostenlose Kreditanfrage</p>
    <h3>Verwendungsmöglichkeit:</h3>
  </aside>
</div>
</body>
</html>
```